Lanterne architecture business cards

We are a new company based in New Zealand. We Specialize in High end Luxury Residential Architecture.

Every home is bespoke and is designed to each clients individual requirements and needs.

I like to design buildings that inspire people through light and form while offering a high level of comfort and usability.

Lines of sight, proportion and balance are fundamental to the spaces I create.
Updates

August 5th is current deadline - Today's date is the 13th of August.

Target Market(s)

New Zealanders who want a custom individual home design, typically 30-65 year old males and females

Industry/Entity Type

Architecture

Contact Information for Business Card

Director - Derek Tolson
Contact Number - 0279164073
Email - info@lanternearchitecture-example.co.nz
Webstie - www.lanternearchitecture-example.co.nz
Social Media - @lanternearchitecture

Font styles to use
Sans Serif

Requirements
Must have
• Logo (Both Sides)
Website
Email
Contact Number
Social Media

Nice to have
• Texture
Should not have
• More than 3 colours - typically I would've thought 2 would be good to match the logo.

```html
<!DOCTYPE html>
<html lang="en">
<head>
<meta charset="utf-8">
<title>Lanterne Architecture – Business Cards</title>
<link href="https://fonts.googleapis.com/css2?family=Montserrat:wght@300;400;500;600&display=swap" rel="stylesheet">
<style>
  :root {
    --backdrop: #d1d2cc;
    --card: #f3f3f1;
    --ink: #1a1a1a;
    --ink-soft: #3a3a3a;
    --rule: #555555;
  }
  * { margin: 0; padding: 0; box-sizing: border-box; }
  html, body {
    width: 1200px;
    height: 1058px;
    overflow: hidden;
    background: var(--backdrop);
    font-family: "Montserrat", Arial, sans-serif;
    color: var(--ink);
  }
  .canvas {
    position: relative;
    width: 1200px;
    height: 1058px;
  }
  .card {
    position: absolute;
    width: 500px;
    height: 306px;
    background: var(--card);
    border: 1px solid #e4e4e0;
  }
  .card--contact { left: 90px; top: 230px; }
  .card--brand { left: 610px; top: 520px; }

  /* Contact side */
  .contact-brand {
    position: absolute;
    left: 0;
    top: 0;
    width: 175px;
    height: 100%;
    display: flex;
    flex-direction: column;
    align-items: center;
    justify-content: center;
    gap: 12px;
  }
  .brand-dot {
    width: 30px;
    height: 30px;
    border-radius: 50%;
    background: var(--ink);
  }
  .brand-name {
    font-weight: 400;
    font-size: 11px;
    letter-spacing: 0.22em;
    text-transform: uppercase;
    color: var(--ink);
    text-align: center;
    line-height: 1.6;
  }
  .divider {
    position: absolute;
    left: 180px;
    top: 98px;
    width: 1px;
    height: 110px;
    background: var(--rule);
  }
  .contact-details {
    position: absolute;
    left: 200px;
    top: 62px;
  }
  .person-name {
    font-weight: 600;
    font-size: 22px;
    letter-spacing: 0.04em;
    text-transform: uppercase;
    color: var(--ink);
    line-height: 1;
  }
  .person-role {
    font-weight: 300;
    font-size: 12px;
    color: var(--ink-soft);
    margin-top: 5px;
  }
  .contact-list {
    list-style: none;
    margin-top: 20px;
    font-weight: 400;
    font-size: 12.5px;
    line-height: 1.45;
    color: var(--ink-soft);
  }

  /* Brand side */
  .card--brand .brand-block {
    position: absolute;
    inset: 0;
    display: flex;
    flex-direction: column;
    align-items: center;
    justify-content: center;
    gap: 22px;
  }
  .card--brand .brand-dot { width: 40px; height: 40px; }
  .card--brand .brand-name {
    font-size: 20px;
    letter-spacing: 0.32em;
  }
</style>
</head>
<body>
  <main class="canvas">
    <section class="card card--contact" aria-label="Business card, contact side">
      <div class="contact-brand">
        <span class="brand-dot"></span>
        <span class="brand-name">Lanterne<br>architecture</span>
      </div>
      <span class="divider"></span>
      <div class="contact-details">
        <h1 class="person-name">Derek Tolson</h1>
        <p class="person-role">Director</p>
        <ul class="contact-list">
          <li>0279164073</li>
          <li>info@lanternearchitecture-example.co.nz</li>
          <li>www.lanternearchitecture-example.co.nz</li>
          <li>@lanternearchitecture</li>
        </ul>
      </div>
    </section>

    <section class="card card--brand" aria-label="Business card, brand side">
      <div class="brand-block">
        <span class="brand-dot"></span>
        <span class="brand-name">Lanterne architecture</span>
      </div>
    </section>
  </main>
</body>
</html>
```